Physician focused educational website needed

We are looking to create a fresh, simple website to help Physicians understand the benefits of protecting their largest asset....their income. We are wanting to create a site that can be a resource to help answer the FAQ that physicians ask regarding Disability Insurance. The goal is not to sell DI but rather to education the physician on the importance of the product and to be a resource for them to learn more.

Target Market(s)

Physicians

Industry/Entity Type

Insurance

Coding

Coded - Design and coding required

Number of Pages Required

1 page

Requirements
Must have
• easy to navigate and understand FAQ format

```html
<!DOCTYPE html>
<html lang="en">
<head>
<meta charset="utf-8">
<title>Steadfast Income – Frequently Asked Question</title>
<link href="https://fonts.googleapis.com/css2?family=Quicksand:wght@400;500;600&display=swap" rel="stylesheet">
<style>
:root{
  --green:#8bc34a;
  --blue:#03a9f4;
  --ink:#222;
  --muted:#666;
  --line:#e6e6e6;
  --row:#f8f8f8;
  --footer:#111;
  --footer-text:#8a8a8a;
  --white:#fff;
}
*{box-sizing:border-box;margin:0;padding:0}
html,body{width:701px;height:1200px;overflow:hidden;background:var(--white)}
body{font-family:"Quicksand",sans-serif;color:var(--ink);position:relative}
.abs{position:absolute}

.topbar{left:0;top:0;width:701px;height:36px;border-bottom:1px solid #ccc;background:var(--white)}
.brand{left:47px;top:11px;font-weight:600;font-size:9.5px;color:#333}
.nav{top:13px;font-size:7.5px;color:#333}
.nav-share{left:572px;top:12px}
.nav-burger{left:680px;top:13px}

.banner{left:0;top:36px;width:701px;height:50px;background:var(--green)}
.banner h1{position:absolute;left:54px;top:14px;font-weight:500;font-size:16.5px;color:var(--white);letter-spacing:.5px}

.crumbs{left:54px;top:96px;font-size:7.5px;color:#555;display:flex;align-items:center;gap:5px}
.crumbs-rule{left:0;top:117px;width:701px;height:1px;background:var(--line)}

.section-title{left:54px;font-size:13.5px;font-weight:500;color:#222}

.faq{left:54px;width:390px;display:flex;align-items:center;padding-left:18px;padding-right:20px;font-size:10px;line-height:10.5px;color:#333}
.faq svg{flex:none;margin-right:10px}
.faq.shaded{background:var(--row)}
.faq.open{background:var(--blue);color:var(--white);display:block;padding:18px 20px 0 18px;box-shadow:0 1px 3px rgba(0,0,0,.15)}
.faq.open .q{font-size:10.4px;line-height:10.5px}
.faq.open .a{margin-top:16px;padding-left:19px;padding-right:0;font-size:7.7px;line-height:15.6px}

.side-menu{left:460px;top:159px;width:187px;border:1px solid var(--green)}
.side-menu li{list-style:none;height:22.4px;line-height:22px;padding-left:8px;font-size:7.6px;color:var(--green);border-top:1px solid var(--green)}
.side-menu li:first-child{border-top:none;background:var(--green);color:var(--white)}

.side-title{left:460px;font-size:12.3px;font-weight:500;color:#222}
.side-list{left:461px;list-style:none}
.side-list li{height:19.2px;display:flex;align-items:center;gap:6px;font-size:7.6px;color:var(--green)}

.footer{left:0;top:977px;width:701px;height:223px;background:var(--footer);color:var(--footer-text)}
.f-head{position:absolute;top:45px;font-size:7.8px;font-weight:600;color:var(--white)}
.f-list{position:absolute;top:60px;list-style:none}
.f-list li{height:18.4px;display:flex;align-items:center;gap:5px;font-size:6.8px}
.f-text{position:absolute;font-size:6.8px;line-height:15.6px}
.socials{position:absolute;left:292px;top:177px;display:flex;gap:7px}
.socials span{width:8px;height:8px;border-radius:50%;background:#9a9a9a}
.copy{position:absolute;left:0;width:701px;top:200px;text-align:center;font-size:6px}
</style>
</head>
<body>

<header class="abs topbar">
  <div class="abs brand">Steadfast Income</div>
  <span class="abs nav" style="left:335px">Disability Insurance</span>
  <span class="abs nav" style="left:418px">Guidelines</span>
  <span class="abs nav" style="left:469px">Faq</span>
  <span class="abs nav" style="left:498px">Contact Us</span>
  <svg class="abs nav-share" width="9" height="9" viewBox="0 0 10 10"><circle cx="8" cy="2" r="1.6" fill="#333"/><circle cx="2" cy="5" r="1.6" fill="#333"/><circle cx="8" cy="8" r="1.6" fill="#333"/><path d="M8 2L2 5L8 8" stroke="#333" stroke-width="1" fill="none"/></svg>
  <span class="abs nav" style="left:608px">Blog</span>
  <svg class="abs nav-burger" width="11" height="9" viewBox="0 0 11 9"><rect width="11" height="1.6" fill="#222"/><rect y="3.7" width="11" height="1.6" fill="#222"/><rect y="7.4" width="11" height="1.6" fill="#222"/></svg>
</header>

<section class="abs banner"><h1>Frequently Asked Question</h1></section>

<nav class="abs crumbs">
  <svg width="9" height="8" viewBox="0 0 10 9"><path d="M1 4.5L5 1L9 4.5M2.5 3.5V8H7.5V3.5" fill="none" stroke="#8bc34a" stroke-width="1.1"/></svg>
  <span style="color:#aaa">/</span><span>FAQ</span>
</nav>
<div class="abs crumbs-rule"></div>

<h2 class="abs section-title" style="top:158px">Section A</h2>

<div class="abs faq open" style="top:182px;height:232px">
  <p class="q"><svg width="9" height="9" viewBox="0 0 9 9" style="margin-right:8px;vertical-align:middle"><rect y="4" width="9" height="1.3" fill="#fff"/></svg>When is the right time to buy Income Protection plan/should I buy while in training/Is there an advantage to buying as a PGY 1?</p>
  <p class="a">The right time to buy insurance is today. Our health can change in an instant so buying coverage while you are young and healthy is imperative. Even as a PGY1, locking in your insurability is important. As more and more residents are starting to take medications for stress and anxiety during these difficult years, your ability to get insurance can be drastically impacted by something that “everyone is doing” just to get by.<br>What matters is that you obtain some form of coverage with the ability to purchase more later regardless of your health. At the very latest, you should make sure you are securing coverage before leaving your training program because you receive significant discounts while in training that you won’t be able to get once you leave.</p>
</div>

<div class="abs faq" style="top:418px;height:48px"><svg width="9" height="9" viewBox="0 0 9 9"><rect y="3.9" width="9" height="1.3" fill="#222"/><rect x="3.9" width="1.3" height="9" fill="#222"/></svg>Wouldn’t my group coverage cover me adequately? (what is the difference between group/private)</div>
<div class="abs faq shaded" style="top:472px;height:48px"><svg width="9" height="9" viewBox="0 0 9 9"><rect y="3.9" width="9" height="1.3" fill="#222"/><rect x="3.9" width="1.3" height="9" fill="#222"/></svg>What features should I look for?</div>
<div class="abs faq" style="top:520px;height:48px"><svg width="9" height="9" viewBox="0 0 9 9"><rect y="3.9" width="9" height="1.3" fill="#222"/><rect x="3.9" width="1.3" height="9" fill="#222"/></svg>What is true own occupation/specialty specific mean?</div>

<h2 class="abs section-title" style="top:587px">Section B</h2>
<div class="abs faq shaded" style="top:612px;height:48px"><svg width="9" height="9" viewBox="0 0 9 9"><rect y="3.9" width="9" height="1.3" fill="#222"/><rect x="3.9" width="1.3" height="9" fill="#222"/></svg>What is Catestrophic Benefit?</div>
<div class="abs faq" style="top:660px;height:48px"><svg width="9" height="9" viewBox="0 0 9 9"><rect y="3.9" width="9" height="1.3" fill="#222"/><rect x="3.9" width="1.3" height="9" fill="#222"/></svg>What is DIRS? (disability income retirement supplement)</div>
<div class="abs faq shaded" style="top:708px;height:46px"><svg width="9" height="9" viewBox="0 0 9 9"><rect y="3.9" width="9" height="1.3" fill="#222"/><rect x="3.9" width="1.3" height="9" fill="#222"/></svg>What if my health changes after I buy coverage?</div>
<div class="abs faq" style="top:754px;height:48px"><svg width="9" height="9" viewBox="0 0 9 9"><rect y="3.9" width="9" height="1.3" fill="#222"/><rect x="3.9" width="1.3" height="9" fill="#222"/></svg>Can I raise my coverage after I enter practice?</div>

<h2 class="abs section-title" style="top:822px">Section C</h2>
<div class="abs faq shaded" style="top:846px;height:48px"><svg width="9" height="9" viewBox="0 0 9 9"><rect y="3.9" width="9" height="1.3" fill="#222"/><rect x="3.9" width="1.3" height="9" fill="#222"/></svg>What is inflation protection? (COLA)</div>
<div class="abs faq" style="top:894px;height:48px"><svg width="9" height="9" viewBox="0 0 9 9"><rect y="3.9" width="9" height="1.3" fill="#222"/><rect x="3.9" width="1.3" height="9" fill="#222"/></svg>Can they raise my rates or cancel me in the future? What if I move, will my discount still apply?</div>

<ul class="abs side-menu">
  <li>Getting Started</li><li>Coverage</li><li>Benefits</li><li>Guide</li><li>Troubleshooting</li><li>Video Tutorials</li>
</ul>

<h3 class="abs side-title" style="top:318px">Recent Blog</h3>
<ul class="abs side-list" style="top:339px">
  <li><svg width="7" height="8" viewBox="0 0 7 8"><path d="M.5.5H4.5L6.5 2.5V7.5H.5Z M2 4H5 M2 5.7H5" fill="none" stroke="#888" stroke-width=".8"/></svg>Lorem ipsum dolor</li>
  <li><svg width="7" height="8" viewBox="0 0 7 8"><path d="M.5.5H4.5L6.5 2.5V7.5H.5Z M2 4H5 M2 5.7H5" fill="none" stroke="#888" stroke-width=".8"/></svg>Lorem ipsum dolor sit amet</li>
  <li><svg width="7" height="8" viewBox="0 0 7 8"><path d="M.5.5H4.5L6.5 2.5V7.5H.5Z M2 4H5 M2 5.7H5" fill="none" stroke="#888" stroke-width=".8"/></svg>Lorem ipsum dolor</li>
  <li><svg width="7" height="8" viewBox="0 0 7 8"><path d="M.5.5H4.5L6.5 2.5V7.5H.5Z M2 4H5 M2 5.7H5" fill="none" stroke="#888" stroke-width=".8"/></svg>Lorem ipsum dolor sit amet</li>
</ul>

<h3 class="abs side-title" style="top:437px">Popular Articles</h3>
<ul class="abs side-list" style="top:458px">
  <li><svg width="7" height="8" viewBox="0 0 7 8"><path d="M.5.5H4.5L6.5 2.5V7.5H.5Z M2 4H5 M2 5.7H5" fill="none" stroke="#888" stroke-width=".8"/></svg>Lorem ipsum dolor sit amet</li>
  <li><svg width="7" height="8" viewBox="0 0 7 8"><path d="M.5.5H4.5L6.5 2.5V7.5H.5Z M2 4H5 M2 5.7H5" fill="none" stroke="#888" stroke-width=".8"/></svg>Lorem ipsum dolor</li>
  <li><svg width="7" height="8" viewBox="0 0 7 8"><path d="M.5.5H4.5L6.5 2.5V7.5H.5Z M2 4H5 M2 5.7H5" fill="none" stroke="#888" stroke-width=".8"/></svg>Lorem ipsum dolor sit amet</li>
  <li><svg width="7" height="8" viewBox="0 0 7 8"><path d="M.5.5H4.5L6.5 2.5V7.5H.5Z M2 4H5 M2 5.7H5" fill="none" stroke="#888" stroke-width=".8"/></svg>Lorem ipsum dolor</li>
</ul>

<footer class="abs footer">
  <h4 class="f-head" style="left:54px">Popular Articles</h4>
  <ul class="f-list" style="left:55px">
    <li><svg width="6" height="7" viewBox="0 0 7 8"><path d="M.5.5H4.5L6.5 2.5V7.5H.5Z" fill="none" stroke="#888" stroke-width=".8"/></svg>Lorem ipsum dolor sit amet</li>
    <li><svg width="6" height="7" viewBox="0 0 7 8"><path d="M.5.5H4.5L6.5 2.5V7.5H.5Z" fill="none" stroke="#888" stroke-width=".8"/></svg>Lorem ipsum dolor</li>
    <li><svg width="6" height="7" viewBox="0 0 7 8"><path d="M.5.5H4.5L6.5 2.5V7.5H.5Z" fill="none" stroke="#888" stroke-width=".8"/></svg>Lorem ipsum dolor sit amet</li>
    <li><svg width="6" height="7" viewBox="0 0 7 8"><path d="M.5.5H4.5L6.5 2.5V7.5H.5Z" fill="none" stroke="#888" stroke-width=".8"/></svg>Lorem ipsum dolor</li>
  </ul>
  <h4 class="f-head" style="left:206px">Recent Blogs</h4>
  <ul class="f-list" style="left:207px">
    <li><svg width="6" height="7" viewBox="0 0 7 8"><path d="M.5.5H4.5L6.5 2.5V7.5H.5Z" fill="none" stroke="#888" stroke-width=".8"/></svg>Lorem ipsum dolor</li>
    <li><svg width="6" height="7" viewBox="0 0 7 8"><path d="M.5.5H4.5L6.5 2.5V7.5H.5Z" fill="none" stroke="#888" stroke-width=".8"/></svg>Lorem ipsum dolor sit amet</li>
    <li><svg width="6" height="7" viewBox="0 0 7 8"><path d="M.5.5H4.5L6.5 2.5V7.5H.5Z" fill="none" stroke="#888" stroke-width=".8"/></svg>Lorem ipsum dolor</li>
    <li><svg width="6" height="7" viewBox="0 0 7 8"><path d="M.5.5H4.5L6.5 2.5V7.5H.5Z" fill="none" stroke="#888" stroke-width=".8"/></svg>Lorem ipsum dolor sit amet</li>
  </ul>
  <h4 class="f-head" style="left:358px">Latest Tweets</h4>
  <p class="f-text" style="left:358px;top:58px">• Lorem ipsum dolor sit amet,<br>consectetur adipiscing elit, sed do...<br>@larkfield http://larkfieldstudio.com<br>• Lorem ipsum dolor sit amet,<br>consectetur adipiscing elit, sed do...<br>@larkfield http://larkfieldstudio.com</p>
  <h4 class="f-head" style="left:510px">Address</h4>
  <p class="f-text" style="left:510px;top:58px">27, Maple Row, Beside Cedar<br>Plaza, Brookdale, Westland<br>482019</p>
  <h4 class="f-head" style="left:510px;top:121px">Email ID</h4>
  <p class="f-text" style="left:510px;top:134px">hello@larkfieldstudio.com</p>
  <div class="socials"><span></span><span></span><span></span><span></span><span></span><span></span><span></span><span></span></div>
  <p class="copy">© 2016 Build By Larkfield Studio</p>
</footer>

</body>
</html>
```